Book Cover Design Project

Design a cover for a children's book. The book is both an educational tool and a Christian devotional. The subject of the book is the biography of Walter Brinkley and contains short descriptions of events from Brinkley's life as well as Christian devotions derived from those events. See attached back-cover material for more information.

Requirements
Must have
• 1. Red, White and Blue for colors.
2. The Tallow Creek Publishing logo which is attached in B&W or color.
3. Title "The Walter Brinkley Devotional: A Guide for Christian Learning"
4. Back cover material which is attached.

```html
<!DOCTYPE html>
<html lang="en">
<head>
<meta charset="UTF-8">
<title>The Walter Brinkley Devotional — Back Cover</title>
<link href="https://fonts.googleapis.com/css2?family=Arimo:wght@400;700&display=swap" rel="stylesheet">
<style>
  :root {
    --red-core: #e3232b;
    --red-deep: #b80f18;
    --red-edge: #a20c14;
    --paper: #ffffff;
    --ink-light: #ffffff;
    --brand-navy: #1f3a6b;
    --brand-dot: #3fae6a;
  }
  * { margin: 0; padding: 0; box-sizing: border-box; }
  html, body { width: 900px; height: 1200px; overflow: hidden; }
  body { font-family: "Arimo", Arial, sans-serif; background: var(--paper); }

  .back-cover {
    position: relative;
    width: 900px;
    height: 1200px;
    overflow: hidden;
    background: radial-gradient(ellipse at 45% 45%, var(--red-core) 0%, var(--red-deep) 70%, var(--red-edge) 100%);
  }

  .facets {
    position: absolute;
    inset: 0;
    width: 900px;
    height: 1200px;
  }

  .blurb {
    position: absolute;
    left: 114px;
    top: 372px;
    width: 676px;
    color: var(--ink-light);
    font-size: 17px;
    line-height: 28.5px;
    text-align: justify;
  }
  .blurb p + p { margin-top: 28px; }

  .imprint-band {
    position: absolute;
    left: 0;
    bottom: 0;
    width: 900px;
    height: 92px;
    background: var(--paper);
  }

  .publisher-mark {
    position: absolute;
    right: 36px;
    top: 24px;
    display: flex;
    align-items: center;
    gap: 10px;
  }
  .publisher-mark .dot {
    width: 22px;
    height: 22px;
    border-radius: 50%;
    background: var(--brand-dot);
  }
  .publisher-mark .name {
    font-family: "Arimo", Arial, sans-serif;
    font-weight: 700;
    font-size: 22px;
    color: var(--brand-navy);
  }
</style>
</head>
<body>
  <main class="back-cover">
    <svg class="facets" viewBox="0 0 900 1200" aria-hidden="true">
      <polygon points="0,0 330,0 900,560 900,700 0,0" fill="#ffffff" opacity="0.07"/>
      <polygon points="0,0 900,700 900,1200 620,1200 0,260" fill="#ffffff" opacity="0.04"/>
      <polygon points="900,420 780,690 900,960" fill="#ffffff" opacity="0.10"/>
      <polygon points="0,540 240,830 0,1110" fill="#000000" opacity="0.05"/>
    </svg>

    <section class="blurb">
      <p>The Walter Brinkley Devotional combines a birth-to-death biography of Walter Brinkley with a Christian children's devotional. The result is a collection of thirty-four lessons which reinforce basic Christian ideals via the true-life stories of one of our nation's most important historical figures. With simple, short readings and introspective follow-up questions, this book will promote spiritual growth while providing in-depth exposure to the life of America's first president. The Walter Brinkley Devotional is appropriate either as a stand-alone personal devotional for children or as a supplement to history/Bible for home-schooling families.</p>
      <p>Best used with children at a third-grade reading level.</p>
    </section>

    <footer class="imprint-band">
      <div class="publisher-mark">
        <span class="dot"></span>
        <span class="name">Tallow Creek Publishing</span>
      </div>
    </footer>
  </main>
</body>
</html>
```